Banner Design for Websites

I am looking for a few various banner designs of the below size. I want them to look authentic, bold and catchy.
Width 939
Height 262
Wording:
WANTED: DRIVEN AND SUCCESSFUL INDIVIDUALS READY TO TAKE THEIR RESULTS TO THE NEXT LEVEL.

Make up to $5000 per sale
No cold calling
No experience required
No pressure selling
NOT MLM

Personal Empowerment. The Next Big Business Boom !

I make well in excess of 10k per month consistently. Brenda K

Some photos attached for use and also some others banners for various workding other than above.

```html
<!DOCTYPE html>
<html lang="en">
<head>
<meta charset="utf-8">
<title>Personal Empowerment Banner</title>
<link rel="stylesheet" href="https://fonts.googleapis.com/css2?family=Alegreya+Sans+SC:ital,wght@0,400;0,500;0,700;1,800&display=swap">
<style>
  :root {
    --pink: #e8197c;
    --magenta: #b7338f;
    --violet: #8a4cae;
    --blue: #3ea6ec;
    --sky: #6fc6f3;
    --white: #ffffff;
    --ribbon-shade: #cfd2d6;
    --gold: #f2c21b;
    --gold-dark: #b57d07;
    --outline: #5a3b05;
    --seal-red: #d61c1c;
    --text-shadow: rgba(40, 10, 60, 0.85);
    --quote-text: #5a2b00;
    --frame: #2b2b2b;
  }
  html, body {
    margin: 0;
    padding: 0;
    overflow: hidden;
    background: #ffffff;
  }
  .banner {
    position: relative;
    width: 1200px;
    height: 335px;
    overflow: hidden;
    font-family: "Alegreya Sans SC", "Trebuchet MS", sans-serif;
    background: linear-gradient(100deg, var(--pink) 0%, var(--magenta) 30%, var(--violet) 52%, var(--blue) 80%, var(--sky) 100%);
  }
  .banner__backdrop {
    position: absolute;
    inset: 0;
  }
  .headline {
    position: absolute;
    left: 0;
    top: 0;
  }
  .seal {
    position: absolute;
    left: -6px;
    top: 112px;
    width: 256px;
    height: 256px;
  }
  .seal__text {
    position: absolute;
    left: 2px;
    top: 204px;
    width: 240px;
    text-align: center;
    color: var(--seal-red);
    text-transform: uppercase;
    font-family: "Trebuchet MS", sans-serif;
  }
  .seal__title {
    display: block;
    font-size: 26px;
    line-height: 30px;
    font-weight: 400;
    margin-bottom: 2px;
  }
  .seal__body {
    display: block;
    font-size: 12.5px;
    line-height: 17px;
    font-weight: 400;
  }
  .benefits {
    position: absolute;
    left: 272px;
    top: 146px;
    margin: 0;
    padding: 0;
    list-style: none;
    color: var(--white);
    font-size: 30px;
    line-height: 35px;
    font-weight: 500;
    text-shadow: 1px 2px 2px var(--text-shadow);
  }
  .benefits__item::before {
    content: "- ";
  }
  .benefits__item--strong {
    text-transform: uppercase;
    font-weight: 700;
    font-family: "Trebuchet MS", sans-serif;
    font-size: 27px;
  }
  .testimonial {
    position: absolute;
    left: 690px;
    top: 238px;
    width: 320px;
    height: 80px;
    background: linear-gradient(180deg, #fff3a2 0%, var(--gold) 55%, #e9a812 100%);
    border: 1px solid var(--gold-dark);
    box-shadow: 0 2px 4px rgba(0,0,0,0.35);
  }
  .testimonial__quote {
    position: absolute;
    left: 62px;
    right: 8px;
    top: 14px;
    margin: 0;
    text-align: center;
    color: var(--quote-text);
    font-size: 16px;
    line-height: 19px;
    font-weight: 500;
  }
  .testimonial__name {
    display: block;
  }
  .award {
    position: absolute;
    left: 700px;
    top: 226px;
    width: 60px;
    height: 104px;
  }
  .portrait {
    position: absolute;
    left: 1004px;
    top: 100px;
    width: 214px;
    height: 250px;
    border-radius: 50%;
    border: 4px solid var(--frame);
    box-sizing: border-box;
    background: radial-gradient(circle at 45% 45%, #c9a98a 0%, #8c6a55 45%, #3d2e2a 100%);
  }
</style>
</head>
<body>
<div class="banner">
  <svg class="banner__backdrop" width="1200" height="335" viewBox="0 0 1200 335" aria-hidden="true">
    <defs>
      <linearGradient id="streak" x1="0" y1="0" x2="1" y2="0">
        <stop offset="0" stop-color="#ffffff" stop-opacity="0"/>
        <stop offset="0.5" stop-color="#ffffff" stop-opacity="0.22"/>
        <stop offset="1" stop-color="#ffffff" stop-opacity="0"/>
      </linearGradient>
    </defs>
    <polygon points="0,40 260,0 330,0 0,110" fill="#ff6fb4" opacity="0.45"/>
    <polygon points="0,150 420,0 470,0 0,190" fill="url(#streak)"/>
    <polygon points="700,335 1200,60 1200,110 780,335" fill="url(#streak)"/>
    <polygon points="860,0 1200,0 1200,40" fill="#ffffff" opacity="0.12"/>
  </svg>

  <svg class="headline" width="1200" height="150" viewBox="0 0 1200 150" role="img" aria-label="Personal Empowerment. The Next Big Business Boom !">
    <defs>
      <linearGradient id="gold-text" x1="0" y1="0" x2="0" y2="1">
        <stop offset="0" stop-color="#fff9a0"/>
        <stop offset="0.5" stop-color="#f6c416"/>
        <stop offset="1" stop-color="#c98508"/>
      </linearGradient>
      <linearGradient id="ribbon-face" x1="0" y1="0" x2="0" y2="1">
        <stop offset="0" stop-color="#ffffff"/>
        <stop offset="1" stop-color="#e2e4e7"/>
      </linearGradient>
    </defs>
    <path d="M236 12 L282 4 L282 88 L236 96 L254 54 Z" fill="var(--ribbon-shade)"/>
    <path d="M852 60 L898 52 L882 96 L898 136 L852 144 Z" fill="var(--ribbon-shade)"/>
    <path d="M270 0 C420 18 640 10 870 0 L870 120 C640 136 420 132 270 112 Z" fill="url(#ribbon-face)" stroke="#c5c8cc" stroke-width="1.5"/>
    <g font-family="'Alegreya Sans SC', sans-serif" font-weight="800" font-style="italic" font-size="40" text-anchor="middle" fill="url(#gold-text)" stroke="var(--outline)" stroke-width="1.4" paint-order="stroke">
      <text x="566" y="44">Personal Empowerment.</text>
      <text x="566" y="104">The Next Big Business Boom !</text>
    </g>
  </svg>

  <svg class="seal" viewBox="0 0 256 256" aria-hidden="true">
    <defs>
      <radialGradient id="seal-gold" cx="0.4" cy="0.35" r="0.7">
        <stop offset="0" stop-color="#fff4a6"/>
        <stop offset="0.6" stop-color="#f2c21b"/>
        <stop offset="1" stop-color="#c88a0a"/>
      </radialGradient>
    </defs>
    <circle cx="128" cy="128" r="126" fill="#b57d07"/>
    <circle cx="128" cy="128" r="120" fill="url(#seal-gold)"/>
    <circle cx="128" cy="128" r="112" fill="none" stroke="#fff2a0" stroke-width="1.5" opacity="0.7"/>
  </svg>
  <div class="seal__text">
    <span class="seal__title">Wanted:</span>
    <span class="seal__body">Driven and<br>successful individuals<br>ready to take their results<br>to the next level.</span>
  </div>

  <ul class="benefits">
    <li class="benefits__item">Make up to $5000 per sale</li>
    <li class="benefits__item">No cold calling</li>
    <li class="benefits__item">No experience required</li>
    <li class="benefits__item">No pressure selling</li>
    <li class="benefits__item benefits__item--strong">Not MLM</li>
  </ul>

  <div class="testimonial">
    <p class="testimonial__quote">I make well in excess of<br>10k per month consistently.<span class="testimonial__name">Brenda K</span></p>
  </div>

  <svg class="award" viewBox="0 0 60 104" aria-hidden="true">
    <path d="M18 44 L6 100 L18 90 L28 102 L30 46 Z" fill="#c4161c"/>
    <path d="M42 44 L54 100 L42 90 L32 102 L30 46 Z" fill="#e0262c"/>
    <circle cx="30" cy="30" r="27" fill="#c4161c"/>
    <circle cx="30" cy="30" r="19" fill="#f2c21b" stroke="#b57d07" stroke-width="2"/>
    <text x="30" y="38" text-anchor="middle" font-family="'Trebuchet MS', sans-serif" font-weight="700" font-size="22" fill="#7a4a00">1</text>
  </svg>

  <div class="portrait" role="img" aria-label="Photo of a smiling couple with their young daughter"></div>
</div>
</body>
</html>
```